Computer Repair Business - Needs New Business Card Design

I want to create a very cool business card for my business. I want to make it 100% different from my previous card. I would like to use similar color scheme like Royal blue.

With this card I want to create a conversation and have my customers say "Wow, that's a cool business card" Trying to prevent it from looking like the typical card that get's shoved into a wallet.

My website is below:

www.milospcworks.com

I want to edit the hours and website and email:

www.milospcworks.com
milo@milospcworks.com

10:30 to 6pm Monday - Friday
10:30 to 3pm Saturday

Just to remind, when i see a new design i don't want to notice my old design.

Business card will be printed and made with rounded corners and horizontal.

The back of the card should say " In-Store Repair, Remote Support, Data Recovery"

Industry/Entity Type

Business

Font styles to use
Sans Serif

Colors
33a6d7
3176b5

Requirements
Must have
• Clean looking - have creative aspects.
Should not have
• Should not look like the previous card design.

```html
<!DOCTYPE html>
<html lang="en">
<head>
<meta charset="utf-8">
<title>Milo's PC Works – Business Card</title>
<link href="https://fonts.googleapis.com/css2?family=Open+Sans:ital,wght@0,400;0,600;1,400&family=Arimo:ital,wght@0,700;1,700&display=swap" rel="stylesheet">
<style>
  :root {
    --royal: #1f4a8f;
    --royal-deep: #17356d;
    --sky: #3176b5;
    --cyan: #33a6d7;
    --ink: #2b2b2b;
    --paper: #ffffff;
    --mist: #e8edf6;
    --backdrop: #e9e7e3;
  }
  * { box-sizing: border-box; margin: 0; padding: 0; }
  html, body { width: 1200px; height: 926px; overflow: hidden; }
  body { background: var(--backdrop); position: relative; font-family: "Open Sans", Arial, sans-serif; }

  .card {
    position: absolute; left: 250px; width: 700px; height: 400px;
    background: var(--paper); box-shadow: 0 6px 18px rgba(0,0,0,.18); overflow: hidden;
    border-radius: 18px;
  }
  .card--front { top: 43px; }
  .card--back { top: 483px; }

  .brand { display: flex; align-items: center; gap: 14px; }
  .brand__name { font-family: "Open Sans", Arial, sans-serif; font-weight: 400; font-size: 34px; letter-spacing: 2px; color: var(--ink); white-space: nowrap; }
  .brand__mark { width: 22px; height: 22px; background: var(--sky); flex: none; }

  /* front */
  .top-band { position: absolute; top: 0; left: 0; right: 0; height: 14px; background: var(--royal); }
  .card--front .brand { position: absolute; top: 42px; left: 36px; }
  .tagline { position: absolute; top: 100px; left: 38px; font-style: italic; font-size: 20px; color: var(--ink); }
  .circuit-art {
    position: absolute; top: 14px; left: 360px; width: 340px; height: 386px;
    background: radial-gradient(circle at 60% 40%, #6f9fe0 0%, #2a5cb3 38%, #10286a 78%, #0a1a47 100%);
    clip-path: polygon(22% 0, 100% 0, 100% 100%, 0 100%, 12% 62%, 0 48%);
  }
  .contact { position: absolute; left: 38px; top: 160px; font-size: 18px; line-height: 27px; color: var(--ink); }
  .contact .web { margin-top: 12px; }
  .partner-band { position: absolute; left: 0; bottom: 0; width: 340px; height: 54px; background: var(--royal); clip-path: polygon(0 0, 92% 0, 100% 100%, 0 100%); }
  .partner-badge { position: absolute; left: 36px; bottom: 14px; width: 190px; height: 26px; background: var(--mist); border-radius: 4px; }

  /* back */
  .circuit-trace {
    position: absolute; top: 22px; right: 28px; width: 300px; height: 80px;
    background: linear-gradient(90deg, rgba(232,237,246,0) 0%, var(--mist) 40%, #d9e0ec 100%);
    border-radius: 6px;
  }
  .services-tab {
    position: absolute; top: 60px; left: 28px; width: 150px; height: 34px;
    background: var(--royal); color: #fff; font-family: "Arimo", Arial, sans-serif; font-weight: 700; font-style: italic;
    font-size: 20px; padding: 4px 0 0 14px; clip-path: polygon(0 0, 100% 0, 92% 100%, 0 100%);
  }
  .services-band { position: absolute; top: 78px; left: 178px; width: 150px; height: 16px; background: var(--royal); }
  .services { position: absolute; top: 110px; left: 28px; width: 300px; list-style: none; }
  .services li {
    font-family: "Arimo", Arial, sans-serif; font-weight: 700; font-style: italic; font-size: 21px; color: var(--royal-deep);
    padding: 7px 0 7px 14px; border-bottom: 1.5px solid var(--sky);
  }
  .hours { position: absolute; top: 130px; left: 350px; width: 330px; text-align: center; font-family: "Arimo", Arial, sans-serif; font-weight: 700; font-size: 22px; line-height: 34px; color: var(--ink); }
  .card--back .brand { position: absolute; top: 268px; left: 0; right: 0; justify-content: center; }
  .card--back .brand__name { font-size: 26px; }
  .card--back .brand__mark { width: 18px; height: 18px; }
  .back-contact { position: absolute; top: 314px; left: 0; right: 0; text-align: center; font-size: 18px; line-height: 27px; color: var(--ink); }
</style>
</head>
<body>
  <section class="card card--front" aria-label="Card front">
    <div class="top-band"></div>
    <div class="circuit-art" role="img" aria-label="Glowing blue circuit board close-up"></div>
    <div class="brand"><span class="brand__name">MILO'S PC WORKS</span><span class="brand__mark"></span></div>
    <p class="tagline">Computer Repair / Sales</p>
    <div class="contact">
      <p>512 Maple Ridge Rd, Fairview</p>
      <p>NJ 07022, 555.014.2287</p>
      <p class="web">www.milospcworks.com</p>
      <p>milo@milospcworks.com</p>
    </div>
    <div class="partner-band"></div>
    <div class="partner-badge" aria-hidden="true"></div>
  </section>

  <section class="card card--back" aria-label="Card back">
    <div class="circuit-trace" role="img" aria-label="Thin grey circuit trace lines with round nodes"></div>
    <div class="services-band"></div>
    <div class="services-tab">Services :</div>
    <ul class="services">
      <li>In-Store Repair</li>
      <li>Remote Support</li>
      <li>Data Recovery</li>
    </ul>
    <div class="hours">
      <p>10:30 to 6pm Monday - Friday</p>
      <p>10:30 to 3pm Saturday</p>
    </div>
    <div class="brand"><span class="brand__name">MILO'S PC WORKS</span><span class="brand__mark"></span></div>
    <div class="back-contact">
      <p>www.milospcworks.com</p>
      <p>milo@milospcworks.com</p>
    </div>
  </section>
</body>
</html>
```